Flyer for spiritual retreat (yoga, meditation, reiki, raw food)

I would like a flyer to promote my upcoming retreat and a matching Facebook banner.

The name of the retreat is "Wavecrest Of Calm" and the tagline is "retreat into you"

The activities in the retreat include daily meditation, ecstatic dance, spiritual development workshops on intuition, energy healing etc and a reiki session is included.

I would like a flyer designed to promote this, something that is editable as I will be running this multiple times and will need to adjust the flyer to add the dates etc each time.

edit: add that here will be fully catered raw food and juices, and that the retreat price includes all accomodation, meals and workshops.

Please contact me if you need further info. Please also visit my website www.marithovland.com and www.facebook.com/tolvanahaven to see my current events and promotions.

Thank you,

Marit

Reason: Hi all, thank you all for your submissions. Apologies as I am traveling and do not have much access to internet and will review your submissions and provide feedback as soon as possible. Kind regards, Marit.

Target Market(s)

People who like meditation, yoga, fans of rowan mabry and jasper vinek, those interested in personal and spiritual development.

Industry/Entity Type

Health And Wellness

Requirements
Must have
• Please put the included reiki session as as added bonus. Something like "BONUS 30 minute reiki healing session" in a little star/banner/something that stands out.
• Please emphasise the "light" part of Wavecrest as I am going for a play on words between in the light and enlightenment.
• Please include placeholder text for place, location, time
• Placeholder for price
• My name (see attached file - can change colour to suit) and website (www.marithovland.com)
Nice to have
• I prefer rounded designs, curves rather than block designs.
Should not have
• Tolvana Haven logo

```html
<!DOCTYPE html>
<html lang="en">
<head>
<meta charset="utf-8">
<title>Wavecrest Of Calm – Retreat Into You</title>
<link rel="stylesheet" href="https://fonts.googleapis.com/css2?family=Great+Vibes&family=Raleway:wght@300;700&family=Crimson+Pro:ital,wght@0,400;0,700;1,400;1,700&family=Pinyon+Script&display=swap">
<style>
  :root {
    --sky-top: #7ba4dd;
    --sky-mid: #7398d1;
    --sky-deep: #4a6ea6;
    --sky-soft: #9ab6e2;
    --sky-pale: #bccff0;
    --ink-white: #ffffff;
    --ink-label: #f1f5fc;
    --ink-signature: #2c2e36;
    --footer-band: #22252d;
    --lotus-tone: #d9e4f6;
    --statue-tone: #2a2c33;
  }
  * { margin: 0; padding: 0; box-sizing: border-box; }
  html, body {
    width: 1072px; height: 1200px; overflow: hidden; background: #ffffff;
  }
  .flyer {
    position: absolute; left: 134px; top: 25px; width: 817px; height: 1154px;
    overflow: hidden;
    background: linear-gradient(180deg,
      var(--sky-top) 0%, var(--sky-mid) 18%, #5a7fb7 27%, var(--sky-deep) 33%,
      #587cb5 40%, #7395cc 52%, var(--sky-soft) 72%, var(--sky-pale) 100%);
    color: var(--ink-white);
  }
  .flyer__curve { position: absolute; left: 0; top: 0; pointer-events: none; }
  .title {
    position: absolute; left: 100px; top: 50px;
    font-family: "Great Vibes", cursive; font-weight: 400;
    font-size: 112px; line-height: 108px; color: var(--ink-white);
    letter-spacing: 1px;
  }
  .title__line { display: block; }
  .title__line--second { padding-left: 60px; }
  .title__light { font-size: 124px; }
  .tagline {
    position: absolute; left: 387px; top: 300px;
    font-family: "Raleway", sans-serif; font-weight: 300;
    font-size: 29px; letter-spacing: 2px; text-transform: uppercase;
  }
  .intro {
    position: absolute; left: 26px; top: 344px; width: 318px;
    font-family: "Crimson Pro", serif; font-style: italic;
    font-size: 21.5px; line-height: 34px;
  }
  .intro strong { font-weight: 700; }
  .brace { position: absolute; left: 350px; top: 346px; }
  .benefits {
    position: absolute; left: 418px; top: 356px; list-style: none;
    font-family: "Crimson Pro", serif; font-size: 24.5px; line-height: 53.5px;
  }
  .benefits li::before { content: "\2733"; font-size: 15px; margin-right: 8px; vertical-align: 3px; }
  .bonus {
    position: absolute; left: 170px; top: 680px; width: 480px; text-align: center;
    font-family: "Crimson Pro", serif; font-weight: 700; font-size: 25px;
  }
  .bonus__rule { position: absolute; left: 168px; top: 716px; }
  .details {
    position: absolute; left: 26px; top: 751px;
    font-family: "Raleway", sans-serif; font-weight: 700; font-size: 15px;
    letter-spacing: 1.5px; color: var(--ink-label);
  }
  .details__row { display: flex; height: 44px; }
  .details__label { width: 76px; }
  .signature {
    position: absolute; right: 70px; top: 740px;
    font-family: "Pinyon Script", cursive; font-size: 60px; color: var(--ink-signature);
  }
  .contact {
    position: absolute; right: 27px; top: 842px; text-align: right;
    font-family: "Crimson Pro", serif; font-size: 25px; line-height: 33px;
  }
  .contact__social { display: inline-flex; align-items: center; gap: 7px; }
  .contact__mark { width: 21px; height: 21px; background: #3f63a8; display: inline-block; }
  .artwork {
    position: absolute; left: 222px; top: 873px; width: 371px; height: 256px;
    border-radius: 50% 50% 0 0 / 70% 70% 0 0;
    background: radial-gradient(ellipse at 50% 80%, var(--statue-tone) 0 18%, rgba(217,228,246,0.75) 19%, rgba(217,228,246,0.25) 70%, transparent 100%);
  }
  .footer-band {
    position: absolute; left: 0; bottom: 0; width: 100%; height: 25px;
    background: var(--footer-band);
  }
</style>
</head>
<body>
  <main class="flyer">
    <svg class="flyer__curve" width="817" height="330" viewBox="0 0 817 330" aria-hidden="true">
      <path d="M0 90 C60 40 120 60 110 120" fill="none" stroke="#ffffff" stroke-width="2" opacity="0.8"/>
      <path d="M817 230 C760 250 700 230 690 200" fill="none" stroke="#ffffff" stroke-width="2" opacity="0.8"/>
    </svg>

    <h1 class="title">
      <span class="title__line">Wave<span class="title__light">crest</span></span>
      <span class="title__line title__line--second">Of Calm</span>
    </h1>
    <p class="tagline">Retreat into you</p>

    <p class="intro">Leave your stresses and worries behind. Come immerse yourself in the bliss of the Transcendental Self. Learn how to integrate this level of awareness into daily living for greater peace, success and happiness in life. In this special <strong>all inclusive</strong> retreat you will gain the benefits of:</p>

    <svg class="brace" width="60" height="300" viewBox="0 0 60 300" aria-hidden="true">
      <path d="M4 4 C40 10 22 60 24 100 C26 130 36 145 56 152 C36 158 26 172 24 200 C22 240 40 290 4 296" fill="none" stroke="#ffffff" stroke-width="2"/>
    </svg>

    <ul class="benefits">
      <li>Daily Meditation Practice</li>
      <li>Ecstatic Dance</li>
      <li>Spiritual Development</li>
      <li>Enhanced Intuition</li>
      <li>Energy Healing</li>
      <li>Fully Catered Raw Food &amp; Juices</li>
    </ul>

    <p class="bonus">BONUS 30 Minute Reiki Healing Session</p>
    <svg class="bonus__rule" width="484" height="8" viewBox="0 0 484 8" aria-hidden="true">
      <path d="M2 4 Q242 0 482 4 Q242 8 2 4 Z" fill="#ffffff"/>
    </svg>

    <dl class="details">
      <div class="details__row"><dt class="details__label">DATE</dt><dd>:</dd></div>
      <div class="details__row"><dt class="details__label">PLACE</dt><dd>:</dd></div>
      <div class="details__row"><dt class="details__label">TIME</dt><dd>:</dd></div>
      <div class="details__row"><dt class="details__label">COST</dt><dd>:</dd></div>
    </dl>

    <p class="signature">Marit Hovland</p>
    <p class="contact">
      www.marithovland.com<br>
      <span class="contact__social"><span class="contact__mark"></span>tolvanahaven</span>
    </p>

    <div class="artwork" role="img" aria-label="Dark seated meditation statue in front of a pale white lotus flower pattern"></div>
    <div class="footer-band"></div>
  </main>
</body>
</html>
```